Flyer Design Project

We are a Human Resources and payroll company with a dedicated staffing and recruiting division. We need a really professional looking and creative flyer that breifly explains our offerings. This flyer will be given to other sales people that sell complementary services to what we offer. Those salespeople will to leave this flyer with prospective clients that want services that do not offer and we do.
Updates

I just uploades our logo in EPS!  Thank you!

Target Market(s)

Employers are our target market. Mostly healthcare but not exclusively.

Industry/Entity Type

It Company

Requirements
Must have
• Photos of people in a working environment would be good. All offering in attached files must be in the flyer as well as our logo.
Nice to have
• It would be nice to convey that we care about our clients and their employees.

```html
<!DOCTYPE html>
<html lang="en">
<head>
<meta charset="utf-8">
<title>HR and Staffing Services Flyer</title>
<link rel="stylesheet" href="https://fonts.googleapis.com/css2?family=Open+Sans:wght@400;700&display=swap">
<style>
  :root {
    --page-bg: #ffffff;
    --panel-light: #f58a2a;
    --panel-mid: #f37022;
    --panel-dark: #ee5a1f;
    --label-red: #e4262a;
    --text-white: #ffffff;
    --bullet-gold: #f9b43a;
    --bullet-shade: #d9841c;
  }
  * { box-sizing: border-box; margin: 0; padding: 0; }
  html, body {
    width: 848px;
    height: 1200px;
    overflow: hidden;
    background: var(--page-bg);
  }
  .flyer {
    position: absolute;
    left: 21px;
    top: 22px;
    width: 806px;
    height: 1158px;
    border-radius: 12px;
    background: radial-gradient(ellipse at 35% 30%, var(--panel-light) 0%, var(--panel-mid) 55%, var(--panel-dark) 100%);
    color: var(--text-white);
    font-family: "Open Sans", Arial, sans-serif;
    font-size: 13.4px;
    line-height: 14.6px;
    letter-spacing: 0.35px;
    padding: 16px 24px 0 22px;
    overflow: hidden;
  }
  .service { margin-bottom: 16px; }
  .service-title, .package-title {
    font-weight: 700;
    font-size: 14px;
    letter-spacing: 0.5px;
  }
  .service-text, .package-note, .package-text {
    text-align: justify;
  }
  .section-label {
    display: inline-block;
    margin: -6px 0 12px -22px;
    padding: 3px 16px 3px 22px;
    width: 308px;
    background: var(--label-red);
    font-weight: 700;
    font-size: 15px;
    line-height: 18px;
    letter-spacing: 0.4px;
  }
  .package { margin-bottom: 15px; }
  .package-list { list-style: none; }
  .package-list li {
    position: relative;
    text-align: justify;
  }
  .package-list li::before {
    content: "";
    position: absolute;
    left: -18px;
    top: 4px;
    width: 9px;
    height: 7px;
    background: linear-gradient(var(--bullet-gold) 55%, var(--bullet-shade) 55%);
  }
  .package-note strong { font-weight: 700; }
</style>
</head>
<body>
<main class="flyer">
  <section class="service">
    <h2 class="service-title">New Hire On-Boarding</h2>
    <p class="service-text">Improve productivity, build loyalty, and increase employee success by creating a positive first impression through an effective and efficient on-boarding process.</p>
  </section>

  <section class="service">
    <h2 class="service-title">Workers Compensation Analysis, Plan Design &amp; Claims Management</h2>
    <p class="service-text">Working with you we will locate the lowest possible rates for your workers compensation insurance needs. We will manage the process with your vendor when injuries occur on the job.</p>
  </section>

  <section class="service">
    <h2 class="service-title">Unemployment Claims Administration</h2>
    <p class="service-text">Many organizations do not realize that their unemployment rate is one area where cost savings can be realized. Through a combination of policy development, employee disciplinary procedures, and a cooperative partnership with the state Unemployment agency we can help to maintain or reduce your unemployment costs.</p>
  </section>

  <section class="service">
    <h2 class="service-title">Regulatory Compliance</h2>
    <p class="service-text">Building off of the HR Audit and Risk Assessment our team will work with you to ensure that you are compliant in federal and state regulatory compliance.</p>
  </section>

  <section class="service">
    <h2 class="service-title">Payroll Administration &amp; Management</h2>
    <p class="service-text">The service removes the worry of payroll and payroll taxes. Direct Deposit makes paying employees both quick and convenient.</p>
  </section>

  <section class="service">
    <h2 class="service-title">OSHA Program Development, Training &amp; Compliance</h2>
    <p class="service-text">The Occupational Safety &amp; Health Administration regulates and enforces federally enacted safety standards for all different types of industries. The healthcare industry has some very specific requirements. We can work with you and your employees to ensure a safe and compliant working environment. This service will include the initial hazard assessment, preparation of your OSHA manual and monthly trainings.</p>
  </section>

  <section class="service">
    <h2 class="service-title">Recruitment &amp; Pre-Employment Services</h2>
    <p class="service-text">Hiring the wrong person costs organizations valuable time and money. By developing and consistently following sound recruitment and pre-employment practices companies find that they are better able to manage their turnover. Our recruitment and pre-employment services include sourcing and prescreening candidates. In partnership with our background investigation organization we will thoroughly screen and advise clients in the hiring process.</p>
  </section>

  <h2 class="section-label">Recruiting and Staffing Packages</h2>

  <section class="package">
    <h3 class="package-title">Package A $275.00</h3>
    <ul class="package-list">
      <li>Source up to 6 resumes</li>
      <li>Position is advertised on 1 job board</li>
    </ul>
    <p class="package-note">Note: Job Description is provided by client. &nbsp;We can provide this service to you for an additional fee of $35)</p>
  </section>

  <section class="package">
    <h3 class="package-title">Package B $ 390.00</h3>
    <ul class="package-list">
      <li>Source up to 8 resumes</li>
      <li>Position advertised on 2 job boards</li>
      <li>Phone screen prospective candidates utilizing position specific requirements and questions provided by Client</li>
      <li>Client will be presented &nbsp;with a summarization of phone screen along with prospective candidates resume</li>
    </ul>
    <p class="package-note"><strong>Note:</strong> Job Description is provided by client. &nbsp;We can provide this service to you for an additional fee of $35)</p>
  </section>

  <section class="package">
    <h3 class="package-title">Package C $ 625.00</h3>
    <ul class="package-list">
      <li>Source up to 10 resumes</li>
      <li>Create a customized job description that best fits your organizations needs</li>
      <li>Position advertised on 3 job boards</li>
      <li>Phone screen prospective candidates and conduct up to 3 in-person interviews based on position specific requirements</li>
      <li>Client will be presented with a summarization of the interviews, based on a candidate ranking system, &nbsp;as well as the prospective candidates resume</li>
    </ul>
  </section>

  <section class="package">
    <h3 class="package-title">Package D Percentage of Prospective Candidates Annual Salary</h3>
    <p class="package-text">Recruiter will take the time to learn about your organization so they can identify individuals with qualities that will best match with your team. &nbsp;They will source, conduct in-depth interviews via phone and in-person, as well as perform thorough background and reference checks prior to employment.</p>
  </section>

  <section class="package">
    <h3 class="package-title">Package also included:</h3>
    <ul class="package-list">
      <li>Create a customized job description that best fits your organizations needs</li>
      <li>Position advertised on 3 job boards</li>
      <li>Client will be presented with a summarization of the interviews, based on a candidate ranking system, &nbsp;as well as the prospective candidates resume</li>
    </ul>
  </section>
</main>
</body>
</html>
```